Business Card Design Project - ol taviran group

dear Sirs

we need business card design for our group ( OL Taviran Group ) , i have got the Logo design of our group from pixel forum in previous , so all need details relating to our group i think available with you, as well as the the chosen logo design

we hope to provide us with business card logo that to be appropaite and satisfactory to us .

thanks

note : logo design of our group is attached .

Reason: please extend the deadline of my project for additional 15 days because i didn't received appropriate design for our gruop yet . kindly beaware that i have received 77 design till now , supossed to send me 200-250 design at least . thanks

contents

name : Selim OR Haddani

position : Operation Manager

• person name

group logo
• logo color matching with back background

```html
<!DOCTYPE html>
<html lang="en">
<head>
<meta charset="utf-8">
<title>OL Taviran Group – Business Card</title>
<link rel="stylesheet" href="https://fonts.googleapis.com/css2?family=Open+Sans:wght@400;600;700&display=swap">
<style>
  :root {
    --stage: #ececec;
    --paper: #ffffff;
    --brand-blue: #0f4f8f;
    --brand-blue-light: #1a74c4;
    --brand-blue-mid: #1b5e9f;
    --ink-light: #ffffff;
    --card-w: 540px;
    --card-h: 310px;
  }
  * { box-sizing: border-box; margin: 0; padding: 0; }
  html, body {
    width: 1200px; height: 758px; overflow: hidden;
    background: var(--stage);
    font-family: "Open Sans", Arial, sans-serif;
  }
  .stage {
    width: 1200px; height: 758px;
    display: flex; align-items: center; justify-content: center; gap: 50px;
  }
  .card {
    width: var(--card-w); height: var(--card-h);
    border-radius: 26px; overflow: hidden; position: relative;
    box-shadow: 0 6px 18px rgba(0,0,0,0.18);
  }
  /* Front */
  .card-front { display: flex; background: var(--paper); }
  .front-brand {
    width: 50%; padding: 0 20px;
    display: flex; align-items: center; justify-content: center;
  }
  .front-details {
    width: 50%; background: var(--brand-blue);
    border-left: 3px solid var(--paper);
    box-shadow: inset 2px 0 0 var(--brand-blue-mid);
    color: var(--ink-light); padding: 52px 26px 0 34px;
  }
  .brand-name {
    font-weight: 700; font-size: 26px; line-height: 1.1;
    color: var(--brand-blue-mid); white-space: nowrap;
  }
  .person-name { font-weight: 700; font-size: 21px; line-height: 1.2; }
  .person-role { font-size: 14px; margin-bottom: 10px; }
  .contact-list { list-style: none; font-size: 13px; line-height: 18px; }
  .contact-list li { display: flex; align-items: center; gap: 7px; }
  .contact-list svg { width: 10px; height: 10px; fill: var(--ink-light); flex: none; }
  .address { font-size: 13px; line-height: 18px; margin-top: 14px; }
  /* Back */
  .card-back {
    background: linear-gradient(100deg, var(--brand-blue) 0%, var(--brand-blue-light) 100%);
    color: var(--ink-light);
    display: flex; flex-direction: column; align-items: center; justify-content: center;
  }
  .back-brand { margin-bottom: 40px; }
  .back-brand .brand-name { color: var(--ink-light); font-size: 42px; }
  .back-web { font-size: 20px; letter-spacing: 1.5px; }
</style>
</head>
<body>
<main class="stage">
  <section class="card card-front" aria-label="Business card front">
    <div class="front-brand">
      <span class="brand-name">OL Taviran Group</span>
    </div>
    <div class="front-details">
      <p class="person-name">Selim OR Haddani</p>
      <p class="person-role">Operation Manager</p>
      <ul class="contact-list">
        <li><svg viewBox="0 0 10 10"><rect x="2.5" y="0" width="5" height="10" rx="1"/></svg>+2347015550142</li>
        <li><svg viewBox="0 0 10 10"><path d="M2 0 L4 2.5 L3 4 Q4.5 6.5 6 7 L7.5 6 L10 8 L8.5 10 Q2 9 0 1.5 Z"/></svg>+2347015550142</li>
        <li><svg viewBox="0 0 10 10"><rect x="0" y="4" width="10" height="6" rx="1"/><rect x="2" y="0" width="6" height="4"/></svg>+2347015550142</li>
        <li><svg viewBox="0 0 10 10"><path d="M0 2 H10 V9 H0 Z M0 2 L5 6 L10 2"/></svg>name@harbelhotels.com</li>
        <li><svg viewBox="0 0 10 10"><circle cx="5" cy="5" r="5"/></svg>www.website.com</li>
      </ul>
      <p class="address">Street name, City<br>State, zip code</p>
    </div>
  </section>
  <section class="card card-back" aria-label="Business card back">
    <div class="back-brand">
      <span class="brand-name">OL Taviran Group</span>
    </div>
    <p class="back-web">www.website.com</p>
  </section>
</main>
</body>
</html>
```